Website Design for Meridel Power Works

We design and install solar power systems for homes and businesses. We also provide engineering services for commercial and utility scale projects

```html
<!DOCTYPE html>
<html lang="en">
<head>
<meta charset="utf-8">
<title>Meridel Power Works</title>
<link href="https://fonts.googleapis.com/css2?family=Roboto:wght@300;400;500&family=Roboto+Condensed:wght@300;400;700&display=swap" rel="stylesheet">
<style>
:root{
  --page:#f1f1ef;
  --ink:#555;
  --muted:#8a8a8a;
  --green:#8cc63f;
  --green-dark:#6ea528;
  --yellow:#fdb913;
  --blue:#17c0f0;
  --purple:#c98be0;
  --form:#dcdcdc;
  --line:#d6d6d6;
  --white:#fff;
}
*{box-sizing:border-box;margin:0;padding:0}
html,body{width:1200px;height:672px;overflow:hidden}
body{background:var(--page);font-family:"Roboto",sans-serif;color:var(--ink);position:relative}

.site-header{position:absolute;left:0;top:0;width:1200px;height:67px;background:var(--white);border-bottom:1px solid var(--line)}
.brand{position:absolute;left:171px;top:24px;display:flex;align-items:center;gap:7px;font-family:"Roboto Condensed",sans-serif;font-weight:700;font-size:13px;line-height:16px;color:#c0392b;letter-spacing:.3px;text-transform:uppercase;white-space:nowrap}
.brand-dot{width:11px;height:11px;border-radius:50%;background:#e8632c}
.main-nav{position:absolute;left:0;top:0;width:1200px;height:67px;font-family:"Roboto Condensed",sans-serif;font-size:13px;color:#8d8d8d;text-transform:uppercase}
.main-nav a{position:absolute;top:31px;color:inherit;text-decoration:none;white-space:nowrap;line-height:15px}
.main-nav a.active{color:#444}
.nav-bar{position:absolute;left:352px;top:53px;width:63px;height:4px;background:var(--green)}
.live-chat{position:absolute;left:881px;top:23px;width:114px;height:31px;background:var(--green);border:1px solid var(--green-dark);border-radius:3px;color:#fff;font-size:13px;font-weight:500;display:flex;align-items:center;justify-content:center;gap:4px}
.live-chat small{font-size:7px;font-weight:400}

.hero{position:absolute;left:148px;top:99px;width:595px;height:261px;background:linear-gradient(120deg,#2e7d1f 0%,#5fb437 40%,#8fd14f 60%,#3c8a25 100%);box-shadow:0 6px 14px rgba(0,0,0,.18)}
.hero-copy{position:absolute;left:240px;top:70px;color:#fff;font-family:"Roboto Condensed",sans-serif;text-transform:uppercase}
.hero-copy h1{font-weight:300;font-size:24px;letter-spacing:.5px}
.hero-copy h1 b{font-weight:400;font-size:38px}
.hero-copy p{font-size:13px;line-height:17px;margin-top:4px;font-weight:300}
.hero-btn{display:inline-block;margin:12px 0 0 152px;background:var(--green-dark);color:#fff;text-transform:none;font-size:14px;padding:6px 14px;border:1px solid #a8dc62}
.dots{position:absolute;right:20px;bottom:14px;display:flex;gap:8px}
.dots i{width:13px;height:13px;border-radius:50%;background:#4fae7a;display:block}
.dots i.on{background:#2b6e3a}

.thumb{position:absolute;border:3px solid #fff;box-shadow:0 2px 6px rgba(0,0,0,.2)}

.card{position:absolute;top:380px;height:104px;color:#fff;border:1px solid rgba(0,0,0,.08);box-shadow:0 8px 10px -6px rgba(0,0,0,.25)}
.card svg{position:absolute;left:30px;top:18px}
.card h2{position:absolute;left:96px;top:15px;font-family:"Roboto Condensed",sans-serif;font-weight:400;font-size:16px;text-transform:uppercase}
.card p{position:absolute;left:96px;top:36px;font-family:"Roboto Condensed",sans-serif;font-size:9px;line-height:16px;text-transform:uppercase;width:165px}
.card .label{position:absolute;left:30px;bottom:9px;font-size:9px;font-weight:500;color:#333;text-transform:uppercase}
.card .more{position:absolute;right:20px;bottom:9px;font-size:9px;color:#444;text-transform:uppercase;display:flex;align-items:center;gap:5px}
.card .more i{width:10px;height:10px;border-radius:50%;background:#444;display:block}
.card-home{left:145px;width:287px;background:var(--green)}
.card-business{left:445px;width:298px;background:var(--yellow)}
.card-quote{left:756px;width:291px;background:var(--blue)}

.rule{position:absolute;left:0;width:1200px;height:1px;background:var(--line)}

.quote-form{position:absolute;left:141px;top:540px;width:644px;height:67px;background:var(--form);font-size:12px;color:#555}
.quote-badge{position:absolute;left:13px;top:12px;width:32px;height:32px;border-radius:50%;background:var(--green);color:#fff;font-size:6px;font-weight:700;display:flex;align-items:center;justify-content:center;text-align:center;line-height:7px;border:2px dotted #fff}
.quote-form h3{position:absolute;left:60px;top:9px;font-weight:400;font-size:12px;color:#999;text-transform:uppercase}
.field{position:absolute;top:28px;height:20px;background:#fff;border:1px solid #c6c6c6;font-size:9px;color:#999;padding:5px 6px;text-transform:uppercase;font-style:italic;white-space:nowrap}
.field-label{position:absolute;top:32px;font-size:12px}
.sign-in{position:absolute;left:560px;top:28px;width:72px;height:20px;background:var(--green);color:#fff;font-size:10px;display:flex;align-items:center;justify-content:center}

.subscribe{position:absolute;left:820px;top:540px;width:219px;height:67px;background:var(--purple);border:1px solid #b77ad0}
.subscribe h3{position:absolute;left:14px;top:11px;font-weight:400;font-size:12px;color:#fff;text-transform:uppercase;display:flex;align-items:center;gap:8px}
.subscribe .field{left:14px;top:33px;width:188px}

.footer-links{position:absolute;left:221px;top:639px;font-size:10px;color:#666}
.footer-links span{margin:0 6px;color:#999}
.social{position:absolute;left:853px;top:634px;display:flex;gap:7px}
.social i{display:block;width:22px;height:22px;border-radius:4px}
</style>
</head>
<body>

<header class="site-header">
  <div class="brand"><span class="brand-dot"></span>Meridel Power Works</div>
  <nav class="main-nav">
    <a class="active" href="#" style="left:368px">Home</a>
    <a href="#" style="left:428px">About Us</a>
    <a href="#" style="left:505px">Services</a>
    <a href="#" style="left:572px">It's all about solar</a>
    <a href="#" style="left:704px">Residential</a>
    <a href="#" style="left:791px">Business</a>
    <span class="nav-bar"></span>
  </nav>
  <div class="live-chat">Live Chat <small>(ONLINE)</small></div>
</header>

<section class="hero" role="img" aria-label="Close-up photo of green grass blades">
  <div class="hero-copy">
    <h1>Start saving <b>Today</b></h1>
    <p>Meridel Power Works is saving your<br>money with a complete solar solution</p>
    <span class="hero-btn">Find out more</span>
  </div>
  <div class="dots"><i></i><i></i><i class="on"></i></div>
</section>

<div class="thumb" style="left:759px;top:99px;width:134px;height:122px;background:linear-gradient(160deg,#9ccf5a,#4f8f2a)" role="img" aria-label="Solar panel lying in the grass"></div>
<div class="thumb" style="left:912px;top:99px;width:135px;height:122px;background:linear-gradient(160deg,#8fc3ea,#2f5f95)" role="img" aria-label="Solar panels under a blue sky"></div>
<div class="thumb" style="left:756px;top:236px;width:137px;height:125px;background:linear-gradient(160deg,#b9c9d6,#4a4f58)" role="img" aria-label="Solar panels on a house roof"></div>
<div class="thumb" style="left:909px;top:236px;width:137px;height:125px;background:linear-gradient(160deg,#9b8a74,#3e5a3c)" role="img" aria-label="Installer with a cap and headphones"></div>

<article class="card card-home">
  <svg width="50" height="46" viewBox="0 0 50 46"><path d="M25 2 2 22h7v22h12V32h8v12h12V22h7z" fill="#fff"/></svg>
  <h2>Resedential</h2>
  <p>Eliminate your electricity bill and avoid future electricity price increases and start saving money</p>
  <span class="label">Resedential</span>
  <span class="more">Read more <i></i></span>
</article>
<article class="card card-business">
  <svg width="54" height="46" viewBox="0 0 54 46"><path d="M19 4h16v6h-4V8h-8v2h-4z" fill="#fff"/><rect x="2" y="12" width="50" height="32" rx="3" fill="#fff"/><rect x="2" y="24" width="50" height="2" fill="#fdb913"/></svg>
  <h2>Business &amp; Gov.</h2>
  <p>We can provide you with a solar system solution to meet your needs</p>
  <span class="label">Business &amp; Gov.</span>
  <span class="more">Read more <i></i></span>
</article>
<article class="card card-quote">
  <svg width="44" height="52" viewBox="0 0 44 52"><path d="M2 2h28l12 12v36H2z" fill="#fff"/><path d="M10 20h24M10 27h24M10 34h24M10 41h16" stroke="#17c0f0" stroke-width="3"/></svg>
  <h2>Free Quote</h2>
  <p>We can provide you with a solar system solution to meet your needs</p>
  <span class="label">Free Quote</span>
  <span class="more">Read more <i></i></span>
</article>

<div class="rule" style="top:517px"></div>

<form class="quote-form">
  <div class="quote-badge">FREE<br>QUOTE</div>
  <h3>Quote Form</h3>
  <span class="field-label" style="left:57px">NAME.:</span>
  <div class="field" style="left:100px;width:157px">Enter your name</div>
  <span class="field-label" style="left:273px">E-mail or phone no.:</span>
  <div class="field" style="left:388px;width:157px">Enter your e-mail adress</div>
  <div class="sign-in">Sign in</div>
</form>

<aside class="subscribe">
  <h3>Subscribe us now
    <svg width="20" height="14" viewBox="0 0 20 14"><rect width="20" height="14" fill="#fff"/><path d="M0 0l10 8 10-8" fill="none" stroke="#c98be0" stroke-width="1.5"/></svg>
  </h3>
  <div class="field">Please enter your e-mail adress</div>
</aside>

<div class="rule" style="top:624px;left:183px;width:827px"></div>

<nav class="footer-links">About<span>|</span>Service<span>|</span>All about solar<span>|</span>Residential<span>|</span>Business<span>|</span>Terms<span>|</span>Support<span>|</span>Privacy<span>|</span>API</nav>

<div class="social">
  <i style="background:#4a9fd8"></i>
  <i style="background:#3b5a98"></i>
  <i style="background:#c4302b"></i>
  <i style="background:#2a4c8c"></i>
  <i style="background:#f08a24"></i>
</div>

</body>
</html>
```